Business card design needed

Our modern electrical contracting company requires business card design utilising our logo and incorporating our tag line "Service when you need it". We specialise in assisting our customers 24/7 offering a breakdown service.

Industry/Entity Type

Electrical

Contact Information for Business Card

Marcus Penhale, Electrical contractor,Tel: (08) 8456 3071, Fax: (08) 8679 4315, Mob 0438 562 740, Email: marcus.penhale@brightwirepower.com.au, Web: www.brightwirepower.com.au

Requirements
Must have
• we require a 2 sided card.
Front- Logo, tag line and contact information.
Rear- service when you need it! Call now for our 24/7 breakdown service

```html
<!DOCTYPE html>
<html lang="en">
<head>
<meta charset="utf-8">
<title>Brightwire Power – Business Cards</title>
<link rel="stylesheet" href="https://fonts.googleapis.com/css2?family=Arimo:wght@400;700&family=Open+Sans:wght@400;600&display=swap">
<style>
  :root {
    --backdrop: #6e4a33;
    --card-white: #ffffff;
    --brand-blue: #1f55b5;
    --band-blue: #0a6ae6;
    --band-blue-deep: #0447b0;
    --band-dark: #111111;
    --band-grey: #6b6b6b;
    --ink: #1e1e1e;
    --ink-soft: #3a3a3a;
    --night: #000000;
    --night-glow: #5a5a5a;
    --mark-grey: #4a4a4a;
  }
  * { box-sizing: border-box; margin: 0; padding: 0; }
  html, body { width: 1200px; height: 742px; overflow: hidden; }
  body { background: var(--backdrop); position: relative; font-family: "Arimo", Arial, sans-serif; }

  .card { position: absolute; width: 534px; height: 305px; overflow: hidden; background: var(--card-white); box-shadow: 0 2px 6px rgba(0,0,0,.35); }
  .card--front { left: 56px; top: 48px; }
  .card--rear-white { left: 623px; top: 55px; }
  .card--rear-pattern { left: 57px; top: 388px; }
  .card--rear-dark { left: 625px; top: 388px; background: radial-gradient(ellipse at 50% 40%, var(--night-glow) 0%, #1c1c1c 55%, var(--night) 85%); }

  .centered { position: absolute; left: 0; right: 0; text-align: center; }

  .brand-dot { position: absolute; left: 50%; border-radius: 50%; transform: translateX(-50%); background: var(--brand-blue); }
  .brand-name { font-family: "Arimo", Arial, sans-serif; font-weight: 700; color: var(--brand-blue); letter-spacing: .5px; }

  /* front */
  .front__dot { top: 16px; width: 70px; height: 70px; }
  .front__name { top: 110px; font-size: 29px; }
  .front__tagline { top: 148px; font-size: 16px; letter-spacing: 1.2px; color: var(--ink); }
  .front__person { position: absolute; left: 0; right: 0; top: 190px; height: 33px; background: linear-gradient(90deg, var(--band-dark) 0%, #2c2c2c 45%, var(--band-grey) 100%); color: #fff; text-align: center; line-height: 33px; font-size: 16px; }
  .front__person strong { font-size: 19px; }
  .front__contacts { position: absolute; left: 0; right: 0; top: 226px; bottom: 0; border-top: 2px solid #fff; background: linear-gradient(180deg, var(--band-blue-deep) 0%, var(--band-blue) 100%); color: #fff; font-size: 14px; }
  .contact-row { position: absolute; left: 0; right: 0; display: flex; justify-content: center; gap: 14px; }
  .contact-row--phones { top: 15px; }
  .contact-row--online { top: 47px; font-size: 13.5px; }
  .contact-item { display: inline-flex; align-items: center; gap: 5px; }
  .contact-item svg { width: 11px; height: 11px; fill: #fff; }

  /* rear cards */
  .rear__dot { top: 30px; width: 96px; height: 96px; }
  .rear__name { top: 140px; font-size: 26px; }
  .rear__lines { font-family: "Open Sans", Arial, sans-serif; font-size: 14px; line-height: 20px; text-transform: uppercase; color: var(--ink); }
  .rear__web { font-family: "Arimo", Arial, sans-serif; font-size: 21px; letter-spacing: 1.5px; color: var(--ink); }
  .card--rear-white .rear__lines { top: 213px; }
  .card--rear-white .rear__web { top: 266px; }

  .pattern-field { position: absolute; inset: 0; background: linear-gradient(180deg, #f3f5f8 0%, #ffffff 50%, #eef1f5 100%); }
  .pattern__name { top: 115px; font-size: 37px; }
  .card--rear-pattern .rear__lines { top: 197px; font-size: 17px; line-height: 24px; color: var(--ink-soft); }
  .card--rear-pattern .rear__web { top: 266px; font-size: 20px; }

  .card--rear-dark .rear__dot { background: var(--mark-grey); }
  .card--rear-dark .rear__name { color: #fff; }
  .card--rear-dark .rear__lines { top: 210px; color: #fff; }
  .card--rear-dark .rear__web { top: 263px; color: #fff; }
</style>
</head>
<body>

<section class="card card--front">
  <span class="brand-dot front__dot"></span>
  <p class="centered brand-name front__name">BRIGHTWIRE POWER</p>
  <p class="centered front__tagline">Service when you need It</p>
  <div class="front__person"><strong>Marcus Penhale,</strong> Electrical contractor</div>
  <div class="front__contacts">
    <div class="contact-row contact-row--phones">
      <span class="contact-item"><svg viewBox="0 0 12 12"><path d="M2.5 0.5l2 2.3-1.1 1.4c.7 1.5 2 2.8 3.5 3.5l1.4-1.1 2.3 2-1.3 2.4C4.6 10.6 1.4 7.4.1 2.8z"/></svg>(08) 8456 3071</span>
      <span class="contact-item"><svg viewBox="0 0 12 12"><rect x="3" y="0" width="6" height="12" rx="1"/><rect x="4" y="1.5" width="4" height="6.5" fill="#0a6ae6"/></svg>0438 562 740</span>
      <span class="contact-item"><svg viewBox="0 0 12 12"><rect x="0" y="5" width="12" height="6" rx="1"/><rect x="3" y="1" width="6" height="4"/></svg>(08) 8679 4315</span>
    </div>
    <div class="contact-row contact-row--online">
      <span class="contact-item"><svg viewBox="0 0 12 12"><rect x="0" y="2" width="12" height="8" rx="1"/><path d="M0.5 2.5L6 7l5.5-4.5" fill="none" stroke="#0a6ae6" stroke-width="1"/></svg>marcus.penhale@brightwirepower.com.au</span>
      <span class="contact-item"><svg viewBox="0 0 12 12"><circle cx="6" cy="6" r="5.5"/><path d="M0.5 6h11M6 .5c-2.5 3-2.5 8 0 11M6 .5c2.5 3 2.5 8 0 11" fill="none" stroke="#0a6ae6" stroke-width=".8"/></svg>www.brightwirepower.com.au</span>
    </div>
  </div>
</section>

<section class="card card--rear-white">
  <span class="brand-dot rear__dot"></span>
  <p class="centered brand-name rear__name">BRIGHTWIRE POWER</p>
  <p class="centered rear__lines">Service when you need it!<br>Call now for our 24/7 breakdown service</p>
  <p class="centered rear__web">www.brightwirepower.com.au</p>
</section>

<section class="card card--rear-pattern">
  <div class="pattern-field" role="img" aria-label="Faint repeating brand pattern in pale grey and blue"></div>
  <p class="centered brand-name pattern__name">BRIGHTWIRE POWER</p>
  <p class="centered rear__lines">Service when you need it!<br>Call now for our 24/7 breakdown service</p>
  <p class="centered rear__web">www.brightwirepower.com.au</p>
</section>

<section class="card card--rear-dark">
  <span class="brand-dot rear__dot"></span>
  <p class="centered brand-name rear__name">BRIGHTWIRE POWER</p>
  <p class="centered rear__lines">Service when you need it!<br>Call now for our 24/7 breakdown service</p>
  <p class="centered rear__web">www.brightwirepower.com.au</p>
</section>

</body>
</html>
```